Wills & Estates legal firm needing A4 presentation folder design

We need a more corporate but family orientated looking presentation folder incorporating existing logo. Needs to be clean lines but warm not clinical. Will contain all documents a family needs when someone dies. Not looking for traditional legal symbols of scales etc. Potential that the design can flow through to letterhead, document front covers, brochures, business cards etc for a complete corporate identity. We are only a firm of one fee earner and cater to a mum and dad market

Industry/Entity Type

Law Firm

Font styles to use
Other font styles liked:
• Univers LT std 57 cn

Colors
ec1f27
848484

Requirements
Must have
• Existing logo
• Area for contact details on back of folder
• Incorporating existing red an grey colours
Should not have
• legal symbols

```html
<!DOCTYPE html>
<html lang="en">
<head>
<meta charset="utf-8">
<title>Kinsford Law – Presentation Folder</title>
<link rel="stylesheet" href="https://fonts.googleapis.com/css2?family=Roboto+Condensed:wght@400&display=swap">
<style>
  :root {
    --backdrop: #b5b5b5;
    --slate: #48535f;
    --slate-deep: #3f4954;
    --brand-red: #c41e2f;
    --paper: #ffffff;
    --paper-shade: #e6e6e6;
    --ink: #2b2b2b;
  }
  html, body {
    margin: 0;
    padding: 0;
    width: 1200px;
    height: 1200px;
    overflow: hidden;
    background: var(--backdrop);
  }
  .folder-sheet {
    position: absolute;
    inset: 0;
    width: 1200px;
    height: 1200px;
    font-family: "Roboto Condensed", "Arial Narrow", sans-serif;
  }
  .brand-name { fill: var(--brand-red); font-weight: 400; }
  .contact-line { fill: var(--ink); font-size: 6.5px; }
  .pocket-copy { fill: var(--ink); font-size: 10px; }
  .slate { fill: var(--slate); }
  .paper { fill: var(--paper); }
  .red-fill { fill: var(--brand-red); }
</style>
</head>
<body>
<svg class="folder-sheet" viewBox="0 0 1200 1200" xmlns="http://www.w3.org/2000/svg">
  <defs>
    <linearGradient id="spine-shade" x1="0" x2="1" y1="0" y2="0">
      <stop offset="0" stop-color="#ffffff" stop-opacity="0"/>
      <stop offset="0.5" stop-color="#d9d9d9"/>
      <stop offset="1" stop-color="#ffffff" stop-opacity="0"/>
    </linearGradient>
  </defs>

  <!-- Outside spread: back cover (left) and front cover (right) -->
  <g class="outside-spread">
    <rect class="back-cover slate" x="260" y="70" width="340" height="440"/>
    <rect class="front-cover slate" x="600" y="70" width="340" height="440"/>

    <!-- Front cover header -->
    <path class="front-header paper" d="M600 70 H940 V216 Q760 250 600 172 Z"/>
    <path class="front-swoosh red-fill" d="M600 172 Q760 250 940 216 V232 Q760 270 600 190 Z"/>
    <text class="brand-name front-logo" x="775" y="148" font-size="32" text-anchor="middle">Kinsford Law</text>

    <!-- Back cover contact corner -->
    <path class="back-corner paper" d="M260 510 V450 Q370 392 460 430 Q522 458 542 510 Z"/>
    <path class="back-swoosh" d="M260 450 Q370 392 460 430 Q522 458 542 510" fill="none" stroke="var(--brand-red)" stroke-width="5"/>
    <text class="brand-name back-logo" x="276" y="484" font-size="17">Kinsford Law</text>
    <g class="contact-block">
      <rect class="red-fill" x="413" y="472" width="5" height="5"/>
      <text class="contact-line" x="421" y="477">(000) 555-0100</text>
      <rect class="red-fill" x="413" y="480" width="5" height="5"/>
      <text class="contact-line" x="421" y="485">hello@kinsford.example</text>
      <rect class="red-fill" x="413" y="488" width="5" height="5"/>
      <text class="contact-line" x="421" y="493">kinsford.example</text>
    </g>
  </g>

  <!-- Inside spread -->
  <g class="inside-spread">
    <rect class="inside-left paper" x="262" y="582" width="336" height="420"/>
    <rect class="inside-right paper" x="598" y="582" width="336" height="420"/>
    <rect class="spine-shadow" x="560" y="582" width="76" height="420" fill="url(#spine-shade)"/>

    <rect class="edge-strip slate" x="262" y="582" width="26" height="250"/>
    <rect class="edge-strip slate" x="908" y="582" width="26" height="250"/>
    <circle class="strip-notch paper" cx="288" cy="724" r="15"/>
    <circle class="strip-notch paper" cx="908" cy="724" r="15"/>

    <path class="pocket-left paper" d="M262 832 H560 Q572 832 575 846 L595 1002 H262 Z" stroke="var(--paper-shade)" stroke-width="1.5"/>
    <path class="pocket-right paper" d="M934 832 H641 Q629 832 626 846 L604 1002 H934 Z" stroke="var(--paper-shade)" stroke-width="1.5"/>

    <g class="pocket-bullets">
      <rect class="red-fill" x="330" y="858" width="4" height="4"/>
      <text class="pocket-copy" x="339" y="863">Lorem Ipsum is simply dummy text of the</text>
      <rect class="red-fill" x="330" y="872" width="4" height="4"/>
      <text class="pocket-copy" x="339" y="877">printing and typesetting industry. Lorem</text>
      <rect class="red-fill" x="330" y="886" width="4" height="4"/>
      <text class="pocket-copy" x="339" y="891">Ipsum has been the industry's standard</text>
      <rect class="red-fill" x="330" y="900" width="4" height="4"/>
      <text class="pocket-copy" x="339" y="905">dummy text ever since the 1500s, when an</text>
      <rect class="red-fill" x="330" y="914" width="4" height="4"/>
      <text class="pocket-copy" x="339" y="919">unknown printer took a galley of type and</text>
    </g>
    <text class="brand-name pocket-logo" x="412" y="972" font-size="28" text-anchor="middle">Kinsford Law</text>
  </g>
</svg>
</body>
</html>
```